We need letterhead, Business Cards, and envelops designed. We have attached a design of our logo and a sample of letterhead idea that was started but never perfected, it is only an idea for the letterhead if you can design something better we may love that also we are open to change.
We want a design that looks professional in style. we are a non profit trade association in the construction industry. the green color in the attached design represent green building, and we like that. also if you just want to enhance the letterhead sample that we attached that would be fine also.
Thanks and good luck
also the name that should show on the first business cards should be Merwin Habsfield, Director are web address is www.tqvmp.org

```html
<!DOCTYPE html>
<html lang="en">
<head>
<meta charset="utf-8">
<title>Envelope Back – Verdant Trades Alliance</title>
<link rel="stylesheet" href="https://fonts.googleapis.com/css2?family=Open+Sans:wght@400&display=swap">
<style>
  :root {
    --paper: #dfebb7;
    --flap: #4a884b;
    --ink: #333333;
  }
  html, body {
    margin: 0;
    padding: 0;
    overflow: hidden;
  }
  .envelope-back {
    position: relative;
    width: 1200px;
    height: 781px;
    background: var(--paper);
    overflow: hidden;
  }
  .envelope-flap {
    position: absolute;
    top: 0;
    left: 0;
    width: 1200px;
    height: 781px;
  }
  .envelope-flap path {
    fill: var(--flap);
  }
  .sender-name {
    position: absolute;
    right: 62px;
    bottom: 52px;
    margin: 0;
    font-family: "Open Sans", Arial, sans-serif;
    font-weight: 400;
    font-size: 30px;
    line-height: 1.2;
    letter-spacing: 0.5px;
    color: var(--ink);
    white-space: nowrap;
  }
</style>
</head>
<body>
  <main class="envelope-back">
    <svg class="envelope-flap" viewBox="0 0 1200 781" aria-hidden="true">
      <path d="M0,0 H1200 C1200,24 1192,35 1182,43 L648,492 Q600,530 552,492 L18,43 C8,35 0,24 0,0 Z"/>
    </svg>
    <p class="sender-name">Verdant Trades Alliance</p>
  </main>
</body>
</html>
```